Dog treat Package Design

We’re looking for a creative and professional designer to develop eye-catching packaging for our upcoming line of premium dog treats under the Tail Nibbles brand.
The design should reflect quality, trust, and natural nutrition, appealing to dog owners who value healthy, high-end pet products.
What We Need
Full packaging design for a resealable stand-up pouch (approx. 130 × 210 + 60 mm)
Front and back layout including space for logo, product name, ingredients, nutrition panel, barcode, and storage instructions
Print-ready files (with dielines, bleeds, and crop marks)
Editable source file (AI / PSD preferred)
3D mock-up or realistic rendering for presentation
Design Direction
Clean, minimal, and modern look with a premium feel
Use natural tones (e.g. earthy browns, creams, muted greens, or soft neutrals)
Should convey trust, wellness, and craftsmanship
Incorporate subtle texture or illustration that hints at natural ingredients or happy, healthy dogs
Must be consistent across potential product variations (e.g. chicken, beef, lamb treats)
Target Audience
Pet owners who value nutrition, quality ingredients, and design aesthetics — typically aged 25–50, with a focus on healthy, Australian-made pet products.
Deliverables
2 initial design concepts
Up to 2 revision rounds
Final deliverables in:
Print-ready PDF (CMYK)
Editable AI/PSD
High-resolution mock-ups
Design style similar to Maple Paws
Updates
Target Market(s)
People with pets - Premium
Look and feel
Each slider illustrates characteristics of the customer's brand and the style your logo design should communicate.

```html
<!DOCTYPE html>
<html lang="en">
<head>
<meta charset="utf-8">
<title>Tail Nibbles Chicken Treats – Pouch Front and Back</title>
<link rel="stylesheet" href="https://fonts.googleapis.com/css2?family=Arvo:wght@400;700&family=Cabin:wght@400;600;700&display=swap">
<style>
  :root{
    --page:#ffffff;
    --cream:#efeddd;
    --cream-light:#f5f3e6;
    --ribbon:#5b5b5b;
    --ribbon-dark:#4a4a4a;
    --tan:#ddb582;
    --peach:#f1c89c;
    --ink:#1e1e1e;
    --ink-soft:#333333;
    --badge:#1f1c1a;
  }
  *{box-sizing:border-box;margin:0;padding:0}
  html,body{width:1200px;height:1200px;overflow:hidden;background:var(--page)}
  body{position:relative;font-family:"Cabin",sans-serif;color:var(--ink)}
  .pouch{position:absolute;top:274px;width:470px;height:702px;background:linear-gradient(180deg,var(--cream-light),var(--cream));overflow:hidden}
  .pouch--front{left:89px}
  .pouch--back{left:638px}
  .zip-line{position:absolute;left:20px;right:20px;top:98px;height:2px;background:#d8d5c4}
  .ribbon{position:absolute;top:0;left:150px;width:172px;height:210px}
  .brand{position:absolute;top:0;left:150px;width:172px;height:200px;display:flex;flex-direction:column;align-items:center;justify-content:center;gap:12px}
  .brand__dot{width:34px;height:34px;border-radius:50%;background:var(--peach)}
  .brand__name{font-family:"Cabin",sans-serif;font-weight:600;font-size:11px;letter-spacing:3px;color:var(--peach)}
  .dog-illustration{position:absolute;left:99px;top:202px;width:280px;height:325px;border-radius:46% 50% 38% 40%;background:radial-gradient(ellipse at 55% 45%,#9a9a96 0%,#5e5e5b 45%,#2c2c2a 75%,rgba(239,237,221,0) 100%)}
  .badge-grain{position:absolute;left:362px;top:150px;width:78px;height:100px}
  .badge-snack{position:absolute;left:333px;top:415px;width:100px;height:100px;border-radius:50%;background:var(--badge);color:var(--tan);font-family:"Arvo",serif;font-size:9.5px;line-height:1.2;display:flex;align-items:center;justify-content:center;text-align:center;transform:rotate(-14deg);padding:10px}
  .product-title{position:absolute;left:0;right:0;top:520px;text-align:center;font-family:"Arvo",serif;font-weight:700;font-size:37px;color:var(--ink)}
  .product-sub{position:absolute;left:0;right:0;top:565px;text-align:center;font-size:16px;line-height:19px;color:var(--ink-soft)}
  .band{position:absolute;left:0;right:0;bottom:0;height:102px}
  .band svg{position:absolute;top:0;left:0}
  .facts{position:absolute;left:0;right:0;bottom:18px;height:60px;display:flex;align-items:center}
  .fact{text-align:center;font-size:14px;color:var(--ink-soft);line-height:17px}
  .fact strong{display:block;font-family:"Arvo",serif;font-weight:700;font-size:17px;color:var(--ink)}
  .fact--reward{width:186px}
  .fact--chicken{width:160px;border-left:1px dashed #8a6c45;border-right:1px dashed #8a6c45}
  .fact--weight{width:70px;font-family:"Arvo",serif;font-weight:700;font-size:18px;color:var(--ink)}
  .story{position:absolute;left:43px;top:225px;width:390px;font-size:14px;line-height:21.5px;color:var(--ink-soft)}
  .story h2{font-size:14px;font-weight:700;color:var(--ink)}
  .story b{font-weight:700;color:var(--ink)}
  .rule{position:absolute;left:50px;right:45px;border-top:1px dotted #666}
  .rule--top{top:390px}
  .rule--bottom{top:473px}
  .claims{position:absolute;left:44px;top:400px;width:390px;height:66px}
  .details{position:absolute;left:50px;top:484px;width:220px;font-size:14px;line-height:16px;color:var(--ink-soft)}
  .details h3{font-size:13px;font-weight:700;color:var(--ink)}
  .band-strip{position:absolute;left:0;right:0;bottom:30px;text-align:center;font-family:"Arvo",serif;font-size:13px;color:var(--ink)}
  .band-strip b{font-weight:700}
</style>
</head>
<body>

<section class="pouch pouch--front" aria-label="Pouch front">
  <div class="zip-line"></div>
  <svg class="ribbon" viewBox="0 0 172 210" aria-hidden="true"><polygon points="0,0 172,0 172,210 90,188 0,210" fill="var(--ribbon)"/></svg>
  <div class="brand"><span class="brand__dot"></span><span class="brand__name">TAIL NIBBLES</span></div>

  <div class="dog-illustration" role="img" aria-label="Engraved-style illustration of a border collie's head"></div>

  <svg class="badge-grain" viewBox="0 0 78 100" aria-label="Grain free">
    <defs><path id="grainArc" d="M6,40 A33,33 0 0 1 72,40"/></defs>
    <text font-family="Arvo, serif" font-size="10" fill="var(--ink)" letter-spacing="1"><textPath href="#grainArc" startOffset="50%" text-anchor="middle">GRAIN FREE</textPath></text>
    <circle cx="39" cy="62" r="33" fill="var(--badge)"/>
    <circle cx="39" cy="62" r="20" fill="none" stroke="var(--tan)" stroke-width="2"/>
    <line x1="25" y1="48" x2="53" y2="76" stroke="var(--tan)" stroke-width="2"/>
    <line x1="39" y1="50" x2="39" y2="76" stroke="var(--tan)" stroke-width="2"/>
  </svg>

  <div class="badge-snack">A wholesome snack, perfect for training or treating Dogs and Pups</div>

  <h1 class="product-title">Chicken Treats</h1>
  <p class="product-sub">Biscuits made with<br>Free-range, Pasture-raised Chicken</p>

  <div class="band">
    <svg width="470" height="102" viewBox="0 0 470 102" aria-hidden="true">
      <path d="M0,10 L10,0 L20,10 L30,0 L40,10 L50,0 L60,10 L70,0 L80,10 L90,0 L100,10 L110,0 L120,10 L130,0 L140,10 L150,0 L160,10 L170,0 L180,10 L190,0 L200,10 L210,0 L220,10 L230,0 L240,10 L250,0 L260,10 L270,0 L280,10 L290,0 L300,10 L310,0 L320,10 L330,0 L340,10 L350,0 L360,10 L370,0 L380,10 L390,0 L400,10 L410,0 L420,10 L430,0 L440,10 L450,0 L460,10 L470,0 L470,102 L0,102 Z" fill="var(--tan)"/>
    </svg>
    <div class="facts">
      <div class="fact fact--reward"><strong>100%</strong>Reward for being a good Dog</div>
      <div class="fact fact--chicken"><strong>100%</strong>Free Range Chicken</div>
      <div class="fact fact--weight">200g</div>
    </div>
  </div>
</section>

<section class="pouch pouch--back" aria-label="Pouch back">
  <div class="zip-line"></div>
  <svg class="ribbon" viewBox="0 0 172 210" aria-hidden="true"><polygon points="0,0 172,0 172,210 90,188 0,210" fill="var(--ribbon)"/></svg>
  <div class="brand"><span class="brand__dot"></span><span class="brand__name">TAIL NIBBLES</span></div>

  <div class="story">
    <h2>Crafted with care:</h2>
    <p>Our <b>Chicken Treats</b> are made from wholesome ingredients - entirely free from Wheat, Sugar, Preservatives, and Artificial Flavours. Created for Training or Indulgence, they’re a pure expression of quality and care. Inspired by our search for healthier options, we handcraft each batch so your pet enjoys only the very best.</p>
  </div>

  <div class="rule rule--top"></div>
  <svg class="claims" viewBox="0 0 390 66" aria-label="Grass fed, hormone free, no added salt, no added spices, no added colourants">
    <g font-family="Arvo, serif" font-size="6.5" font-weight="700" fill="var(--ink)" text-anchor="middle">
      <text x="30" y="8">GRASS FED</text>
      <text x="105" y="8">HORMONE FREE</text>
      <text x="185" y="8">NO ADDED SALT</text>
      <text x="265" y="8">NO ADDED SPICES</text>
      <text x="345" y="8">NO ADDED COLOURANTS</text>
    </g>
    <g fill="var(--badge)">
      <circle cx="30" cy="38" r="22"/><circle cx="105" cy="38" r="22"/><circle cx="185" cy="38" r="22"/><circle cx="265" cy="38" r="22"/><circle cx="345" cy="38" r="22"/>
    </g>
    <g stroke="var(--tan)" stroke-width="2" fill="none" stroke-linecap="round">
      <path d="M20,48 L24,30 M28,48 L30,26 M34,48 L38,30 M18,48 L42,48"/>
      <path d="M94,49 L116,27 M100,33 L110,43 M112,27 L118,33"/>
      <circle cx="185" cy="38" r="13"/><line x1="176" y1="29" x2="194" y2="47"/>
      <path d="M258,46 L272,30 M255,43 a5,5 0 1 0 7,7 Z"/>
      <path d="M338,44 a5,5 0 0 0 10,0 L343,32 Z M352,30 L352,48"/>
    </g>
  </svg>
  <div class="rule rule--bottom"></div>

  <div class="details">
    <h3>Ingredients:</h3>
    <p>100% Free-range, Pasture Raised Chicken &amp; Potassium Sorbate</p>
    <h3>Contact:</h3>
    <p>Tail Nibbles<br>www.tailnibbles.example</p>
  </div>

  <div class="band">
    <svg width="470" height="102" viewBox="0 0 470 102" aria-hidden="true">
      <path d="M0,10 L10,0 L20,10 L30,0 L40,10 L50,0 L60,10 L70,0 L80,10 L90,0 L100,10 L110,0 L120,10 L130,0 L140,10 L150,0 L160,10 L170,0 L180,10 L190,0 L200,10 L210,0 L220,10 L230,0 L240,10 L250,0 L260,10 L270,0 L280,10 L290,0 L300,10 L310,0 L320,10 L330,0 L340,10 L350,0 L360,10 L370,0 L380,10 L390,0 L400,10 L410,0 L420,10 L430,0 L440,10 L450,0 L460,10 L470,0 L470,102 L0,102 Z" fill="var(--tan)"/>
    </svg>
    <p class="band-strip">Tail Nibbles <b>Chicken</b> Treats • Tail Nibbles <b>Chicken</b> Treats</p>
  </div>
</section>

</body>
</html>
```